Kestrel Bridge Consulting (KBC) Business Card Design

I would like to create double-sided business cards that contain:
1) Name: Derek Molvane
2) Phone Number: +1 (555) 218-4907
3) Email: Derek.Molvane@KestrelBridgeConsulting.example
4) Website: KestrelBridgeConsulting.example

I would like to include my logo and a color scheme similar to the Varnholt Grand Prix Ostera squad color scheme (black, silver, greenish-blue – but can also include regular blue)

What we do: Our company develops and delivers innovative and pragmatic information technology and cybersecurity risk and compliance solutions for organizations in the commercial market as well as the federal, and state/local sectors.

```html
<!DOCTYPE html>
<html lang="en">
<head>
<meta charset="UTF-8">
<title>Kestrel Bridge Consulting – Business Card</title>
<link href="https://fonts.googleapis.com/css2?family=Chakra+Petch:wght@400;500;700&display=swap" rel="stylesheet">
<style>
  :root {
    --backdrop: #737373;
    --card-dark: #1f1c19;
    --card-dark-edge: #25211d;
    --card-light: #ebebeb;
    --teal: #1ec6c6;
    --ink: #2a2a2a;
    --white: #ffffff;
  }
  html, body {
    margin: 0;
    padding: 0;
    width: 1200px;
    height: 1000px;
    overflow: hidden;
    background: var(--backdrop);
    font-family: "Chakra Petch", sans-serif;
  }
  .card {
    position: absolute;
    left: 294px;
    width: 613px;
    height: 352px;
    border-bottom-right-radius: 86px;
    overflow: hidden;
    box-shadow: 0 6px 14px rgba(0,0,0,0.28);
  }
  .card--back { top: 121px; background: var(--card-dark); }
  .card--front { top: 516px; background: var(--card-light); }

  .back-texture {
    position: absolute;
    inset: 0;
    background:
      radial-gradient(circle at 30% 30%, rgba(255,255,255,0.035), transparent 60%),
      linear-gradient(135deg, var(--card-dark) 0%, var(--card-dark-edge) 100%);
  }

  .wordmark {
    position: absolute;
    display: flex;
    align-items: center;
    gap: 10px;
  }
  .wordmark__dot {
    width: 54px;
    height: 54px;
    border-radius: 50%;
    background: var(--teal);
    flex: none;
  }
  .wordmark__name {
    font-weight: 500;
    font-size: 17px;
    line-height: 17px;
    letter-spacing: 0.5px;
    text-transform: uppercase;
    border-left: 1.5px solid currentColor;
    padding-left: 5px;
  }
  .card--back .wordmark { left: 311px; top: 214px; }
  .card--back .wordmark__name { color: var(--white); }
  .card--front .wordmark { left: 36px; top: 40px; }
  .card--front .wordmark__name { color: #111; }

  .front-glow {
    position: absolute;
    left: 290px;
    top: 0;
    width: 323px;
    height: 352px;
    background: radial-gradient(ellipse at 70% 50%, rgba(30,198,198,0.28) 0%, rgba(30,198,198,0.12) 45%, transparent 75%);
  }

  .holder-name {
    position: absolute;
    left: 36px;
    top: 166px;
    margin: 0;
    font-weight: 700;
    font-size: 26px;
    letter-spacing: 1px;
    color: var(--teal);
    text-transform: uppercase;
  }
  .contact-list {
    position: absolute;
    left: 36px;
    top: 232px;
    margin: 0;
    padding: 0;
    list-style: none;
  }
  .contact-list li {
    display: flex;
    align-items: center;
    gap: 7px;
    height: 28px;
    font-size: 18px;
    color: var(--ink);
  }
  .contact-icon {
    width: 22px;
    height: 22px;
    flex: none;
  }
</style>
</head>
<body>
  <section class="card card--back">
    <div class="back-texture" role="img" aria-label="Subtle embossed repeating brand pattern on dark card"></div>
    <div class="wordmark">
      <span class="wordmark__dot"></span>
      <span class="wordmark__name">Kestrel<br>Bridge<br>Consulting</span>
    </div>
  </section>

  <section class="card card--front">
    <div class="front-glow" role="img" aria-label="Large faint speckled brand emblem in teal"></div>
    <div class="wordmark">
      <span class="wordmark__dot"></span>
      <span class="wordmark__name">Kestrel<br>Bridge<br>Consulting</span>
    </div>
    <h1 class="holder-name">Derek Molvane</h1>
    <ul class="contact-list">
      <li>
        <svg class="contact-icon" viewBox="0 0 22 22"><circle cx="11" cy="11" r="11" fill="#1ec6c6"/><path d="M7.5 6.5c.6-.6 1.3-.5 1.6.1l.8 1.6c.2.5 0 .9-.4 1.2l-.5.4c.5 1.2 1.5 2.2 2.7 2.7l.4-.5c.3-.4.8-.6 1.2-.4l1.6.8c.6.3.7 1 .1 1.6-.8.8-2 1-3.1.4-2.1-1.1-3.7-2.7-4.8-4.8-.6-1.1-.4-2.3.4-3.1z" fill="#fff"/></svg>
        +1 (555) 218-4907
      </li>
      <li>
        <svg class="contact-icon" viewBox="0 0 22 22"><circle cx="11" cy="11" r="11" fill="#1ec6c6"/><rect x="6" y="7.5" width="10" height="7" fill="none" stroke="#fff" stroke-width="1.3"/><path d="M6 7.5l5 4 5-4" fill="none" stroke="#fff" stroke-width="1.3"/></svg>
        derek.molvane@kestrelbridgeconsulting.example
      </li>
      <li>
        <svg class="contact-icon" viewBox="0 0 22 22"><circle cx="11" cy="11" r="11" fill="#1ec6c6"/><g fill="none" stroke="#fff" stroke-width="1.1"><circle cx="11" cy="11" r="5"/><ellipse cx="11" cy="11" rx="2.2" ry="5"/><path d="M6 11h10M7 8.3h8M7 13.7h8"/></g></svg>
        kestrelbridgeconsulting.example
      </li>
    </ul>
  </section>
</body>
</html>
```